Website for enterprise software start-up

We need a new Wordpress website. We are an early stage start-up focused on mobile video technology for cellular operators. The audience is strategy, marketing and customer acquisition execs from the operators.

The purpose of the site is to act as a sales brochure and capture leads. A demo app can be downloaded from the current site, want to put that behind a contact form.

Current website is at www.brevlane.tv. Similar number of pages. Looking for a clean design template, with minimal customization. Blog will remain as is.

Want to be able to modify the copy via Wordpress. Reference designs I like: tarnwick.com, tessel4analytics.com

Target Market(s)

Mobile operators and MVNOs in the US and Asia Pacific regions

Industry/Entity Type

Business Software

Coding

Coded - Design and coding required

Number of Pages Required

4 page

Font styles to use
Sans Serif

Colors
f78f20

Requirements
Must have
• Form for downloading sample apps.
• Landing page with image, Product, Blog, About, Contact
• Team page

```html
<!DOCTYPE html>
<html lang="en">
<head>
<meta charset="utf-8">
<title>Brevlane Media — Mobile Video Engagement</title>
<link rel="stylesheet" href="https://fonts.googleapis.com/css2?family=Roboto:wght@400;500;700&family=Lato:wght@400;700&display=swap">
<style>
:root{
  --orange:#f78f20;
  --orange-dark:#e0760c;
  --ink:#1e1e1e;
  --text:#444;
  --muted:#777;
  --line:#d6d6d6;
  --panel:#ececec;
  --panel-2:#e2e2e2;
  --cream:#fdf2e7;
  --white:#fff;
  --night:#0c0c0c;
}
*{box-sizing:border-box;margin:0;padding:0}
html,body{width:1200px;height:3750px;overflow:hidden}
body{position:relative;font-family:"Lato",Arial,sans-serif;color:var(--text);background:var(--white)}
a{text-decoration:none}
.abs{position:absolute}
h2.section-title{position:absolute;left:0;width:1200px;text-align:center;font-family:"Roboto",Arial,sans-serif;font-weight:500;font-size:29px;color:var(--ink);letter-spacing:.5px}
h2.section-title span{color:var(--orange)}
.title-rule{position:absolute;height:1px;background:var(--line)}

/* header */
.site-header{position:absolute;left:0;top:0;width:1200px;height:65px;background:var(--white)}
.brand{position:absolute;left:100px;top:10px;display:flex;align-items:center;gap:10px}
.brand-mark{width:34px;height:34px;background:var(--orange)}
.brand-name{font-family:"Roboto",Arial,sans-serif;font-weight:700;font-size:36px;color:var(--ink);line-height:1;letter-spacing:-.5px}
.main-nav{position:absolute;right:95px;top:0;display:flex;gap:46px;height:65px;align-items:center}
.main-nav a{font-family:"Roboto",Arial,sans-serif;font-size:15px;color:var(--ink);position:relative;height:65px;line-height:65px}
.main-nav a.active{color:var(--orange)}
.main-nav a.active::after{content:"";position:absolute;left:-8px;right:-8px;bottom:0;height:3px;background:var(--orange)}

/* hero */
.hero{position:absolute;left:0;top:65px;width:1200px;height:473px;background:radial-gradient(ellipse at 60% 40%,#3b3430 0%,#1d1a18 55%,#0d0c0b 100%)}
.hero-title{position:absolute;top:100px;width:1200px;text-align:center;font-family:"Roboto",Arial,sans-serif;font-weight:500;font-size:38px;color:var(--white)}
.hero-sub{position:absolute;top:178px;left:310px;width:580px;text-align:center;font-family:"Roboto",Arial,sans-serif;font-size:20px;line-height:32px;color:#eee}
.btn{display:block;background:var(--orange);color:var(--white);text-align:center;font-family:"Roboto",Arial,sans-serif;font-weight:500}
.hero .btn{position:absolute;left:483px;top:280px;width:234px;height:50px;line-height:50px;font-size:19px;border-radius:3px}
.dots{position:absolute;top:354px;left:570px;display:flex;gap:8px}
.dots i{width:11px;height:11px;border-radius:50%;background:var(--white)}
.dots i.on{background:transparent;border:2px solid var(--white)}

/* about */
.about-copy{position:absolute;left:110px;top:636px;width:980px;text-align:center;font-size:12.5px;line-height:19px;color:#555}

/* feature panels */
.panel{position:absolute;left:0;width:1200px;background:linear-gradient(160deg,#f0f0f0 0%,#e4e4e4 50%,#efefef 100%)}
.feature-title{position:absolute;font-family:"Roboto",Arial,sans-serif;font-weight:500;font-size:26px;color:var(--orange);letter-spacing:.5px}
.feature-intro{position:absolute;font-size:15px;color:#333}
.feature-list{position:absolute;list-style:none}
.feature-list li{position:relative;height:50px;margin-bottom:20px;background:var(--white);display:flex;align-items:center;font-size:13.5px;color:#333;padding-left:68px;padding-right:16px;line-height:18px}
.feature-list .icon{position:absolute;left:0;top:0;width:50px;height:50px;background:var(--orange);display:flex;align-items:center;justify-content:center}
.device-art{position:absolute;border-radius:34px}

/* clients */
.client-strip{position:absolute;top:2165px;left:100px;width:1000px;display:flex;justify-content:space-between}
.client{width:155px;height:77px;border:1px solid var(--line);display:flex;align-items:center;justify-content:center;gap:8px;font-family:"Lato",Arial,sans-serif;font-weight:700;font-size:15px;color:#666}
.client b{width:12px;height:12px;background:#999;display:inline-block}
.arrow{position:absolute;top:2186px;width:32px;height:34px;background:#ddd;display:flex;align-items:center;justify-content:center}
.partner-badge{position:absolute;left:478px;top:2290px;width:244px;height:92px;border-radius:10px;background:linear-gradient(#f6f6f6,#e3e3e3);border:1px solid #cfcfcf}
.partner-badge::before{content:"";position:absolute;left:0;top:0;width:92px;height:92px;border-radius:10px;background:#1f6fd1}
.partner-note{position:absolute;top:2395px;width:1200px;text-align:center;font-size:13px;color:#333}
.partner-note a{color:var(--orange)}

/* team */
.team{position:absolute;left:0;top:2457px;width:1200px;height:370px;background:var(--cream)}
.member{position:absolute;top:118px;width:338px;height:213px;background:var(--white);box-shadow:0 1px 4px rgba(0,0,0,.08)}
.member .portrait{position:absolute;left:-87px;top:20px;width:180px;height:175px;background:linear-gradient(#7b7b7b,#3f4a55)}
.member h3{position:absolute;left:125px;top:30px;font-family:"Roboto",Arial,sans-serif;font-weight:500;font-size:22px;color:var(--orange)}
.member .role{position:absolute;left:125px;top:64px;font-size:14px;color:#333}
.member .mail{position:absolute;left:125px;top:100px;font-size:12.5px;color:#555;display:flex;align-items:center;gap:8px}
.member .mail i{width:18px;height:13px;background:var(--orange);display:inline-block}
.socials{display:flex;gap:10px}
.socials span{width:30px;height:30px;background:var(--orange);display:block}
.member .socials{position:absolute;left:125px;top:140px}

/* inquiry */
.inquiry{position:absolute;left:0;top:2827px;width:1200px;height:528px;background:radial-gradient(ellipse at 50% 60%,#262626 0%,#111 60%,#050505 100%)}
.inquiry .section-title{color:var(--white)}
.field{position:absolute;border:1px solid #888;border-radius:4px;background:rgba(0,0,0,.35);font-style:italic;font-size:13px;color:#bbb;padding:12px 0 0 36px}
.field-icon{position:absolute;width:46px;height:46px;border-radius:50%;background:#1b1b1b;border:2px solid #bbb;display:flex;align-items:center;justify-content:center}
.inquiry .btn{position:absolute;left:548px;top:435px;width:152px;height:45px;line-height:45px;font-size:15px;border-radius:2px}

/* sample apps */
.apps{position:absolute;left:0;top:3355px;width:1200px;height:265px;background:linear-gradient(#e9ecef,#dde1e5)}
.store{position:absolute;top:145px;height:55px;border-radius:3px;background:var(--orange);color:var(--white);display:flex;align-items:center;gap:12px;padding-left:14px;font-family:"Roboto",Arial,sans-serif}
.store i{width:26px;height:26px;background:var(--white);border-radius:50%;display:block}
.store small{display:block;font-size:11px;line-height:13px}
.store strong{display:block;font-size:17px;font-weight:500;line-height:20px}

/* footer */
.site-footer{position:absolute;left:0;top:3620px;width:1200px;height:130px;background:var(--night)}
.site-footer .socials{position:absolute;left:522px;top:32px}
.copyright{position:absolute;top:86px;width:1200px;text-align:center;font-size:12.5px;color:#bbb}
</style>
</head>
<body>

<header class="site-header">
  <div class="brand"><span class="brand-mark"></span><span class="brand-name">brevlane</span></div>
  <nav class="main-nav">
    <a class="active" href="#">HOME</a><a href="#">PRODUCT</a><a href="#">BLOG</a><a href="#">ABOUT US</a><a href="#">OUR TEAM</a><a href="#">CONTACT US</a>
  </nav>
</header>

<section class="hero" role="img" aria-label="Dark blurred photo of a hand holding a phone in a dim room">
  <h1 class="hero-title">High Quality Mobile Engagement</h1>
  <p class="hero-sub">We Engage Mobile Audiences With The Right Video Content At The Perfect Moment</p>
  <a class="btn" href="#">GET STARTED</a>
  <div class="dots"><i class="on"></i><i></i><i></i><i></i></div>
</section>

<section class="about">
  <h2 class="section-title" style="top:566px">ABOUT <span>BREVLANE MEDIA</span></h2>
  <div class="title-rule" style="left:430px;width:340px;top:612px"></div>
  <p class="about-copy">Lorem ipsum dolor sit amet, consectetuer adipiscing elit, sed diam nonummy nibh euismod tincidunt ut laoreet dolore magna aliquam erat volutpat. Ut wisi enim ad minim veniam, quis nostrud exerci tation ullamcorper suscipit lobortis nisl ut aliquip ex ea commodo consequat. Duis autem vel eum iriure dolor in hendrerit in vulputate velit esse molestie consequat, vel illum dolore eu feugiat nulla facilisis at vero eros et accumsan et iusto odio dignissim qui blandit praesent</p>
</section>

<section class="panel" style="top:742px;height:685px">
  <div class="device-art" role="img" aria-label="White smartphone showing a lock screen with a video push notification" style="left:110px;top:58px;width:280px;height:575px;background:linear-gradient(#f4f4f4,#d9d9d9);border:2px solid #c9c9c9"></div>
  <div class="abs" style="left:132px;top:140px;width:236px;height:414px;background:linear-gradient(#3a3440,#1c1a22)" role="img" aria-label="Phone lock screen"></div>
  <h2 class="feature-title" style="left:442px;top:116px">PUSH VIDEO NOTIFICATIONS</h2>
  <div class="title-rule" style="left:442px;width:460px;top:163px"></div>
  <p class="feature-intro" style="left:442px;top:185px">Personalised flawless HD videos, revealed at the perfect moment, as rich media notifications.</p>
  <ul class="feature-list" style="left:442px;top:233px;width:658px">
    <li><span class="icon"><svg width="28" height="20" viewBox="0 0 28 20" fill="none" stroke="#fff" stroke-width="2"><rect x="1" y="3" width="18" height="14" rx="2"/><path d="M19 8l7-4v12l-7-4z"/></svg></span>Reach your mobile audience with beautiful HD thumbnails and in-notification videos.</li>
    <li><span class="icon"><svg width="26" height="26" viewBox="0 0 26 26" fill="none" stroke="#fff" stroke-width="2"><circle cx="13" cy="13" r="11"/><path d="M10 8l8 5-8 5z"/></svg></span>Instant video playback, zero buffering, guaranteed flawless playback - even when offline.</li>
    <li><span class="icon"><svg width="24" height="24" viewBox="0 0 24 24" fill="none" stroke="#fff" stroke-width="2"><path d="M4 20l2-6L17 3l4 4L10 18z"/><path d="M4 20l6-2"/></svg></span>Content is personalised based on viewer interests and mobile viewing habits.</li>
    <li><span class="icon"><svg width="20" height="26" viewBox="0 0 20 26" fill="none" stroke="#fff" stroke-width="2"><rect x="2" y="1" width="16" height="24" rx="2"/><path d="M6 7h8M6 12h8M6 17h5"/></svg></span>Monetize with beautiful HD preroll or interstitial ads.</li>
    <li><span class="icon"><svg width="26" height="26" viewBox="0 0 26 26" fill="none" stroke="#fff" stroke-width="2"><circle cx="13" cy="13" r="11"/><path d="M13 6v7l5 3"/></svg></span>Easily added to your existing apps within one hour.</li>
  </ul>
</section>

<section class="panel" style="top:1427px;height:623px;background:linear-gradient(200deg,#e6e6e6 0%,#dedede 50%,#ebebeb 100%)">
  <h2 class="feature-title" style="left:100px;top:77px">NATIVE PUSH VIDEO</h2>
  <div class="title-rule" style="left:100px;width:380px;top:120px"></div>
  <p class="feature-intro" style="left:100px;top:150px">Personalised flawless HD videos, discoverable in-app, and playable even when offline.</p>
  <ul class="feature-list" style="left:100px;top:193px;width:590px">
    <li><span class="icon"><svg width="28" height="20" viewBox="0 0 28 20" fill="none" stroke="#fff" stroke-width="2"><rect x="1" y="3" width="18" height="14" rx="2"/><path d="M19 8l7-4v12l-7-4z"/></svg></span>Guarantee your audience never gets frustrated with a poor quality mobile video streaming experience.</li>
    <li><span class="icon"><svg width="26" height="26" viewBox="0 0 26 26" fill="none" stroke="#fff" stroke-width="2"><circle cx="13" cy="13" r="11"/><path d="M10 8l8 5-8 5z"/></svg></span>Instant video playback, zero buffering, HD quality guaranteed - even when offline.</li>
    <li><span class="icon"><svg width="24" height="24" viewBox="0 0 24 24" fill="none" stroke="#fff" stroke-width="2"><path d="M4 20l2-6L17 3l4 4L10 18z"/><path d="M4 20l6-2"/></svg></span>Content is personalised based on viewer interests and mobile viewing habits.</li>
    <li><span class="icon"><svg width="20" height="26" viewBox="0 0 20 26" fill="none" stroke="#fff" stroke-width="2"><rect x="2" y="1" width="16" height="24" rx="2"/><path d="M6 7h8M6 12h8M6 17h5"/></svg></span>Monetize with beautiful HD preroll or interstitial ads.</li>
    <li><span class="icon"><svg width="26" height="24" viewBox="0 0 26 24" fill="none" stroke="#fff" stroke-width="2"><rect x="2" y="2" width="22" height="6"/><rect x="2" y="9" width="22" height="6"/><rect x="2" y="16" width="22" height="6"/></svg></span>Use your existing content management and hosting systems.</li>
  </ul>
  <div class="device-art" role="img" aria-label="Two smartphones, white and blue, showing a movie trailers app" style="left:745px;top:80px;width:140px;height:480px;background:linear-gradient(#f2f2f2,#cfcfcf);border:2px solid #bbb"></div>
  <div class="device-art" style="left:862px;top:62px;width:236px;height:500px;background:linear-gradient(#2d2d2d,#151515);border:5px solid #2fa8e0" role="img" aria-label="Movie trailers list on phone screen"></div>
</section>

<section class="clients">
  <h2 class="section-title" style="top:2088px">OUR <span>CLIENTS</span></h2>
  <div class="title-rule" style="left:435px;width:330px;top:2135px"></div>
  <div class="arrow" style="left:42px"><svg width="10" height="14" viewBox="0 0 10 14" fill="none" stroke="#888" stroke-width="2"><path d="M8 1L2 7l6 6"/></svg></div>
  <div class="client-strip">
    <div class="client">Corvane TV</div>
    <div class="client"><b></b>Quillara</div>
    <div class="client">Thornbay</div>
    <div class="client">Corvane TV</div>
    <div class="client" style="font-size:12px">Halden Music Group</div>
  </div>
  <div class="arrow" style="left:1126px"><svg width="10" height="14" viewBox="0 0 10 14" fill="none" stroke="#888" stroke-width="2"><path d="M2 1l6 6-6 6"/></svg></div>
  <div class="partner-badge" role="img" aria-label="Certified developer partner badge"></div>
  <p class="partner-note"><a href="#">Contact us</a> for details of how to become a Certified Developer Partner.</p>
</section>

<section class="team">
  <h2 class="section-title" style="top:30px">OUR <span>TEAMS</span></h2>
  <div class="title-rule" style="left:435px;width:330px;top:78px"></div>
  <article class="member" style="left:232px">
    <div class="portrait" role="img" aria-label="Portrait photo of Martin"></div>
    <h3>MARTIN</h3>
    <p class="role">Lorem ipsum dolor sit amet</p>
    <p class="mail"><i></i>info@Loremipsumdolor.com</p>
    <div class="socials"><span></span><span></span><span></span><span></span></div>
  </article>
  <article class="member" style="left:717px">
    <div class="portrait" role="img" aria-label="Portrait photo of Owen"></div>
    <h3>OWEN</h3>
    <p class="role">Lorem ipsum dolor sit amet</p>
    <p class="mail"><i></i>info@Loremipsumdolor.com</p>
    <div class="socials"><span></span><span></span><span></span><span></span></div>
  </article>
</section>

<section class="inquiry" role="img" aria-label="Dark photo background of a hand using a phone">
  <h2 class="section-title" style="top:30px">QUICK <span>INQUIRY</span></h2>
  <div class="title-rule" style="left:435px;width:330px;top:78px;background:#555"></div>
  <div class="field" style="left:243px;top:148px;width:350px;height:42px">Name</div>
  <div class="field-icon" style="left:200px;top:146px"><svg width="22" height="22" viewBox="0 0 22 22" fill="#ddd"><circle cx="9" cy="7" r="4"/><path d="M1 20c0-5 4-7 8-7s8 2 8 7z"/></svg></div>
  <div class="field" style="left:643px;top:148px;width:352px;height:42px">Email</div>
  <div class="field-icon" style="left:613px;top:146px"><svg width="22" height="16" viewBox="0 0 22 16" fill="none" stroke="#ddd" stroke-width="2"><rect x="1" y="1" width="20" height="14"/><path d="M1 1l10 8 10-8"/></svg></div>
  <div class="field" style="left:243px;top:222px;width:752px;height:186px">Message</div>
  <div class="field-icon" style="left:200px;top:220px"><svg width="20" height="20" viewBox="0 0 20 20" fill="#ddd"><path d="M1 9L19 1l-6 18-3-7z"/></svg></div>
  <a class="btn" href="#">SEND MESSAGE</a>
</section>

<section class="apps" role="img" aria-label="Faded photo of a phone in hand behind the download buttons">
  <h2 class="section-title" style="top:66px">SAMPLE <span>APPS</span></h2>
  <div class="title-rule" style="left:435px;width:330px;top:112px;background:#c4c8cc"></div>
  <a class="store" href="#" style="left:387px;width:193px"><i></i><span><small>Available On</small><strong>APP VAULT</strong></span></a>
  <a class="store" href="#" style="left:597px;width:215px"><i></i><span><small>Handset App On</small><strong>DROID SHELF</strong></span></a>
</section>

<footer class="site-footer">
  <div class="socials"><span></span><span></span><span></span><span></span></div>
  <p class="copyright">Copyright © 2016 Brevlane Media. All Rights Reserved.</p>
</footer>

</body>
</html>
```